Events By Quellon

Weddings, Corporate, Special Events
Memorable Catering, Personalized Menus, Custom Layout & Designs
Professional Staff, Excellent Service
Our Mission is Turning YOUR Vision into a Reality

Dorrie Quellon, Principal Planner
ph. 202 555-0187 - fax 301-555-0142
Email - eventsbyquellon@mailhaven.net
Web - www.cateringbyquellon.net
cateringbyquellon@Instagram

Target Market(s)

All Brides, Corprate Business, Special Events

Industry/Entity Type

Hospitality

Contact Information for Business Card

clean but affective

Font styles to use
Serif
Sans Serif
Script

Colors

Designer to choose colors to be used in the design.

Requirements
Must have
• logo with tagline using colors that will enhance what
• some pictures of nice table scape, hors d'oevures, upscale foods......
Nice to have
• Event: Something that happens or is regarded as happening, an occurrence especially one of some importance.
Should not have
• Use Logo on both sides

```html
<!DOCTYPE html>
<html lang="en">
<head>
<meta charset="utf-8">
<title>Events By Quellon – Business Card</title>
<link href="https://fonts.googleapis.com/css2?family=Roboto:ital,wght@0,400;0,500;1,400&display=swap" rel="stylesheet">
<style>
  :root {
    --teal: #17aebb;
    --grey: #8a8a8a;
    --grey-light: #b9b9b9;
    --paper: #e6e6e6;
    --card-white: #ffffff;
    --night: #141816;
    --text-light: #e9e9e9;
  }
  * { margin: 0; padding: 0; box-sizing: border-box; }
  html, body { width: 1200px; height: 960px; overflow: hidden; }
  body { background: var(--paper); position: relative; font-family: "Roboto", Arial, sans-serif; }

  .card { position: absolute; width: 600px; height: 343px; overflow: hidden; }
  .card-front { left: 314px; top: 113px; background: var(--card-white); }
  .card-back { left: 311px; top: 472px; background: var(--night); }

  .card-art { position: absolute; inset: 0; width: 100%; height: 100%; }

  .brand-name {
    font-family: "Roboto", Arial, sans-serif; font-weight: 500;
    color: var(--teal); font-size: 23px; white-space: nowrap;
  }

  .brand-front { position: absolute; left: 20px; top: 118px; width: 240px; text-align: center; }
  .brand-tagline {
    font-family: "Roboto", Arial, sans-serif; font-weight: 400;
    font-size: 9.5px; color: var(--grey); margin-top: 5px;
  }

  .brand-back { position: absolute; left: 50px; top: 130px; width: 240px; text-align: center; }
  .brand-back .brand-name { font-size: 23px; }

  .contact { position: absolute; left: 313px; top: 74px; }
  .contact-name { color: var(--teal); font-size: 22px; font-weight: 500; line-height: 1.1; }
  .contact-title { color: var(--grey-light); font-size: 14.5px; margin-bottom: 12px; }
  .contact-list { list-style: none; }
  .contact-list li {
    display: flex; align-items: center; gap: 9px;
    color: var(--text-light); font-size: 14.5px; line-height: 19px;
  }
  .contact-list svg { width: 12px; height: 12px; flex: none; fill: var(--teal); }

  .definition-band {
    position: absolute; left: 0; top: 268px; width: 100%; height: 57px;
    background: rgba(23, 174, 187, 0.45);
    display: flex; align-items: center; justify-content: center; text-align: center;
    color: #ffffff; font-style: italic; font-size: 15px; line-height: 19px;
  }
</style>
</head>
<body>

<section class="card card-front" aria-label="Business card front">
  <svg class="card-art" viewBox="0 0 600 343" preserveAspectRatio="none">
    <defs>
      <radialGradient id="bouquet" cx="0.75" cy="0.45" r="0.6">
        <stop offset="0" stop-color="#f6c9c6"/>
        <stop offset="0.55" stop-color="#f1d3bd"/>
        <stop offset="1" stop-color="#e8c9a2"/>
      </radialGradient>
      <linearGradient id="front-white" x1="0" y1="0" x2="1" y2="1">
        <stop offset="0" stop-color="#ffffff"/>
        <stop offset="1" stop-color="#ececec"/>
      </linearGradient>
    </defs>
    <rect width="600" height="343" fill="url(#bouquet)" role="img" aria-label="Photo of a pink rose and hydrangea table bouquet"/>
    <path d="M0 0 L328 0 C300 80 326 150 298 208 C240 258 118 250 88 343 L0 343 Z" fill="url(#front-white)"/>
    <path d="M298 0 L306 0 C286 40 290 70 275 95" fill="none" stroke="#8f8f8f" stroke-width="3"/>
    <path d="M328 0 L346 0 C332 90 346 160 320 226 C260 282 132 272 110 343 L86 343 C108 254 232 254 294 206 C320 150 300 80 328 0 Z" fill="var(--teal)"/>
    <path d="M96 240 C80 270 72 305 72 343 L78 343 C80 305 88 272 100 244 Z" fill="#8f8f8f"/>
  </svg>
  <div class="brand-front">
    <div class="brand-name">Events By Quellon</div>
    <div class="brand-tagline">Events Designed with You in mind</div>
  </div>
</section>

<section class="card card-back" aria-label="Business card back">
  <svg class="card-art" viewBox="0 0 600 343" preserveAspectRatio="none">
    <defs>
      <linearGradient id="buffet" x1="0" y1="0" x2="1" y2="1">
        <stop offset="0" stop-color="#2a2e29"/>
        <stop offset="0.5" stop-color="#1a1d19"/>
        <stop offset="1" stop-color="#262a22"/>
      </linearGradient>
    </defs>
    <rect width="600" height="343" fill="url(#buffet)" role="img" aria-label="Dimmed photo of a catered buffet with olives, salads and hors d'oeuvres"/>
  </svg>

  <div class="brand-back">
    <div class="brand-name">Events By Quellon</div>
  </div>

  <div class="contact">
    <div class="contact-name">Dorrie Quellon</div>
    <div class="contact-title">Principal Planner</div>
    <ul class="contact-list">
      <li><svg viewBox="0 0 12 12"><path d="M2.5 0.5 L4.5 0.5 L5.2 3.2 L3.8 4.4 C4.5 6 6 7.5 7.6 8.2 L8.8 6.8 L11.5 7.5 L11.5 9.5 C11.5 10.6 10.6 11.5 9.5 11.5 C4.6 11.5 0.5 7.4 0.5 2.5 C0.5 1.4 1.4 0.5 2.5 0.5 Z"/></svg>202 555-0187</li>
      <li><svg viewBox="0 0 12 12"><rect x="3" y="0.5" width="6" height="3"/><rect x="0.5" y="4" width="11" height="5" rx="1"/><rect x="3" y="8" width="6" height="3.5"/></svg>301-555-0142</li>
      <li><svg viewBox="0 0 12 12"><path d="M0.5 2 L11.5 2 L11.5 3 L6 6.5 L0.5 3 Z M0.5 4.3 L6 7.8 L11.5 4.3 L11.5 10 L0.5 10 Z"/></svg>cateringbyquellon@mailhaven.net</li>
      <li><svg viewBox="0 0 12 12"><circle cx="6" cy="6" r="5.5"/><path d="M6 0.5 V11.5 M0.5 6 H11.5" stroke="#1a1d19" stroke-width="0.8"/></svg>www.eventsbyquellon.net</li>
      <li><svg viewBox="0 0 12 12"><rect x="0.5" y="0.5" width="11" height="11" rx="2"/></svg>@ cateringbyquellon</li>
    </ul>
  </div>

  <p class="definition-band">Event: Something that happens or is regarded as happening,<br>an occurrence especially one of some importance.</p>
</section>

</body>
</html>
```